SNOW PLOW DOOR HANGERS

The Door Hangers will be 3.75" wide x 8.75" long. The door hander will be hung using a rubber band. Please use entire 3.75"x8.75 for entire design

These Door hangers will advertise Snow Plowing for residential driveways.
Flyer to say:

Dalvin Snow Powing

24/7 availability
Price per push
Price per season
Place in phone number: use 555-382-7146 for now.

Target Market(s)

customers seeking to have their driveways plowed.

Industry/Entity Type

Rubber

Requirements
Must have
• The Door Hangers will be 3.75" wide x 8.75" long. The door hander will be hung using a rubber band. Please use entire 3.75"x8.75 for entire design
• These Door hangers will advertise Snow Plowing for residential driveways.
• Flyer to say:
• Dalvin Snow Powing
• 24/7 availability
• Price per push
• Price per season
• Place in phone number: use 555-382-7146 for now.

```html
<!DOCTYPE html>
<html lang="en">
<head>
<meta charset="UTF-8">
<title>Dalvin Snow Powing – Door Hanger</title>
<link href="https://fonts.googleapis.com/css2?family=Anton&family=Bodoni+Moda:wght@600&display=swap" rel="stylesheet">
<style>
  :root {
    --canvas-bg: #e9e7e4;
    --hanger-crimson: #9a1a46;
    --hanger-crimson-deep: #7d1238;
    --panel-pink: rgba(255, 214, 226, 0.38);
    --headline-yellow: #f6e62c;
    --band-yellow: #f7ea22;
    --phone-blue: #1d2f86;
    --text-shadow: rgba(60, 0, 20, 0.55);
  }
  * { box-sizing: border-box; margin: 0; padding: 0; }
  html, body {
    width: 800px;
    height: 1200px;
    overflow: hidden;
    background: var(--canvas-bg);
  }
  .door-hanger {
    position: absolute;
    left: 165px;
    top: 51px;
    width: 470px;
    height: 1097px;
    background: linear-gradient(160deg, var(--hanger-crimson) 0%, var(--hanger-crimson-deep) 100%);
    overflow: hidden;
    box-shadow: 0 6px 22px rgba(0,0,0,0.18);
  }
  .hanger-hole {
    position: absolute;
    left: 50%;
    top: 28px;
    width: 26px;
    height: 26px;
    margin-left: -13px;
    border-radius: 50%;
    background: var(--canvas-bg);
    box-shadow: inset 0 1px 3px rgba(0,0,0,0.4);
  }
  .brand-name, .brand-service, .availability-hours, .phone-number {
    font-family: "Anton", "Impact", sans-serif;
    text-transform: uppercase;
    text-align: center;
  }
  .brand-name {
    position: absolute;
    top: 74px;
    width: 100%;
    font-size: 134px;
    line-height: 1;
    letter-spacing: 2px;
    color: var(--headline-yellow);
    text-shadow: 3px 3px 0 var(--text-shadow);
  }
  .brand-service {
    position: absolute;
    top: 212px;
    width: 100%;
    font-size: 66px;
    line-height: 1;
    color: var(--headline-yellow);
    text-shadow: 2px 2px 0 var(--text-shadow);
  }
  .offer-panel {
    position: absolute;
    left: 34px;
    right: 34px;
    top: 312px;
    height: 612px;
    border-radius: 14px;
    background: var(--panel-pink);
    text-align: center;
    padding-top: 36px;
  }
  .availability-hours {
    font-size: 100px;
    line-height: 1;
    color: var(--headline-yellow);
    text-shadow: 3px 3px 0 var(--text-shadow);
    margin-bottom: 18px;
  }
  .offer-list { list-style: none; }
  .offer-item {
    font-family: "Bodoni Moda", "Georgia", serif;
    font-weight: 600;
    font-size: 62px;
    line-height: 1;
    color: var(--headline-yellow);
    text-shadow: 2px 2px 0 var(--text-shadow);
    margin-bottom: 52px;
    transform: scaleX(0.82);
  }
  .phone-band {
    position: absolute;
    left: 0;
    bottom: 0;
    width: 100%;
    height: 118px;
    background: var(--band-yellow);
    display: flex;
    align-items: center;
    justify-content: center;
  }
  .phone-number {
    font-size: 80px;
    line-height: 1;
    color: var(--phone-blue);
    letter-spacing: 1px;
  }
</style>
</head>
<body>
  <div class="door-hanger">
    <div class="hanger-hole"></div>
    <h1 class="brand-name">Dalvin</h1>
    <p class="brand-service">Snow Powing</p>
    <div class="offer-panel">
      <p class="availability-hours">24/7</p>
      <ul class="offer-list">
        <li class="offer-item">Availability</li>
        <li class="offer-item">Price per push</li>
        <li class="offer-item">Price per season</li>
      </ul>
    </div>
    <div class="phone-band">
      <p class="phone-number">555-382-7146</p>
    </div>
  </div>
</body>
</html>
```